flyer for letter box drop 2012

Advertising flyer that is delivered to homes in our suburb.
We are optometrists and looking to have a flyer delivered into our local area residential letterboxes. As a business that has been in the area for 25 years we are looking for an innovative approach to keeping our existing customers as well as appealing to the new generation.
We would like the flyer to reflect or professional eye care services
and commitment to quality service and products.
We do not promote our selves as a discount outlet for eg 2 for 1,50% of everything.
I have attached a copy of the flyer we have been using for the last 12 months.

Target Market(s)

25- 70 year olds male and female

Industry/Entity Type

Residential

Requirements
Must have
• flyer should be double sided a5 page
Prominent logo display
address ,phone number , web address,

```html
<!DOCTYPE html>
<html lang="en">
<head>
<meta charset="utf-8">
<title>Harlow Lane Optical – Flyer</title>
<link rel="stylesheet" href="https://fonts.googleapis.com/css2?family=Open+Sans:wght@400;700&display=swap">
<style>
  :root {
    --brand-blue: #1a1fb8;
    --panel-pink: #ff12d8;
    --panel-green: #66ff3d;
    --page-border: #bdbdbd;
    --white: #ffffff;
    --photo-light: #e9e4df;
    --photo-mid: #b9977c;
    --photo-dark: #5a4434;
  }
  * { box-sizing: border-box; margin: 0; padding: 0; }
  html, body { width: 1200px; height: 852px; overflow: hidden; background: var(--white); }
  body { position: relative; font-family: "Open Sans", Verdana, sans-serif; }

  .page {
    position: absolute; top: 25px; width: 567px; height: 803px;
    border: 1px solid var(--page-border); background: var(--white); overflow: hidden;
  }
  .page--front { left: 16px; }
  .page--back { left: 604px; }

  /* Business name */
  .business-name {
    position: absolute; left: 0; width: 100%; text-align: center;
    color: var(--brand-blue); font-weight: 400; line-height: 1.1; white-space: nowrap;
  }
  .page--front .business-name { top: 196px; font-size: 50px; letter-spacing: -0.5px; }
  .page--back .business-name { top: 742px; font-size: 24px; }

  /* Panels */
  .panel {
    position: absolute; left: 0; top: 402px; width: 100%; height: 294px;
    border-radius: 0 36px 0 36px; color: var(--white); font-weight: 700;
  }
  .panel--services { background: var(--panel-pink); padding: 14px 24px 0 27px; }
  .panel--faq { background: var(--panel-green); padding: 14px 24px 0 25px; }
  .panel__title { font-size: 23px; letter-spacing: 0.6px; }
  .panel__subtitle { font-size: 16.5px; margin-top: 2px; letter-spacing: 0.5px; }

  .services { list-style: none; margin-top: 12px; font-size: 14px; line-height: 19px; letter-spacing: 0.45px; padding-right: 60px; }
  .services > li { position: relative; padding-left: 18px; }
  .services .tick { position: absolute; left: 0; top: 6px; width: 9px; height: 8px; }
  .checks { list-style: none; font-weight: 400; font-size: 12px; line-height: 15.5px; margin: 1px 0 1px; letter-spacing: 0.4px; }
  .checks li { position: relative; padding-left: 12px; }
  .checks li::before { content: ""; position: absolute; left: 2px; top: 4px; width: 7px; height: 7px; border-radius: 50%; background: var(--white); }

  .faq { margin-top: 8px; padding-right: 6px; }
  .faq__q { font-size: 14.5px; line-height: 17px; letter-spacing: 0.5px; }
  .faq__a { font-weight: 400; font-size: 11.5px; line-height: 14px; letter-spacing: 0.45px; margin-bottom: 9px; }

  .contact { position: absolute; left: 0; top: 736px; width: 100%; text-align: center; color: var(--brand-blue); font-size: 11.5px; line-height: 15px; }
  .contact strong { font-weight: 700; }

  .photo {
    position: absolute; left: 0; top: 0; width: 100%; height: 402px;
    background: radial-gradient(ellipse 45% 60% at 50% 45%, var(--photo-mid) 0%, var(--photo-dark) 55%, var(--photo-light) 85%), var(--photo-light);
  }
</style>
</head>
<body>
  <section class="page page--front">
    <p class="business-name">Harlow Lane Optical</p>

    <div class="panel panel--services">
      <h2 class="panel__title">Independent Optometrists</h2>
      <p class="panel__subtitle">Servicing Brookvale since 1989</p>
      <ul class="services">
        <li><svg class="tick" viewBox="0 0 9 8"><path d="M1 4 L3.5 6.5 L8 1" fill="none" stroke="#fff" stroke-width="1.8"/></svg>Healthcover bulk billed eye examinations
          <ul class="checks">
            <li>Glaucoma assessment</li>
            <li>Diabetes vision assessment</li>
            <li>Cataract assessment</li>
            <li>Macula degeneration assessment</li>
            <li>Retinal photography</li>
          </ul>
        </li>
        <li><svg class="tick" viewBox="0 0 9 8"><path d="M1 4 L3.5 6.5 L8 1" fill="none" stroke="#fff" stroke-width="1.8"/></svg>Latest spectacle and contact lenses</li>
        <li><svg class="tick" viewBox="0 0 9 8"><path d="M1 4 L3.5 6.5 L8 1" fill="none" stroke="#fff" stroke-width="1.8"/></svg>Qualified and experienced Optometrist and Optical Technician in store</li>
        <li><svg class="tick" viewBox="0 0 9 8"><path d="M1 4 L3.5 6.5 L8 1" fill="none" stroke="#fff" stroke-width="1.8"/></svg>Direct billing to private health funds with ClaimPoint</li>
        <li><svg class="tick" viewBox="0 0 9 8"><path d="M1 4 L3.5 6.5 L8 1" fill="none" stroke="#fff" stroke-width="1.8"/></svg>On site lens fittings to own frames</li>
      </ul>
    </div>

    <p class="contact">14b Harlow Lane, Brookvale <strong>Tel: 9100 4823</strong> www.harlowlaneoptical.com.au<br><strong>Optometrists: Daniel Ferris and Sophie Marlow</strong></p>
  </section>

  <section class="page page--back">
    <div class="photo" role="img" aria-label="Photograph of a young woman adjusting black-framed glasses"></div>

    <div class="panel panel--faq">
      <h2 class="panel__title">Frequently Asked Questions</h2>
      <div class="faq">
        <p class="faq__q">Do all optical outlets sell the same spectacle lenses?</p>
        <p class="faq__a">No. Advances in modern technology have allowed the introduction of new spectacle lens designs which offer better vision. At Harlow Lane Optical we choose value lenses based on their ability to best enhance your sight.</p>
        <p class="faq__q">If I want new prescription lenses fitted to my existing pair of glasses, do I have to go without them for a week?</p>
        <p class="faq__a">No. This is not the case at Harlow Lane Optical. New lenses can be fitted onsite within 1 hour.</p>
        <p class="faq__q">Do I have to purchase my spectacles where my private health fund directs ?</p>
        <p class="faq__a">No. It is your decision where to have your eyes tested and where to purchase your spectacles or contact lenses. We can direct bill your private health fund with the CLAIMPOINT system.</p>
      </div>
    </div>

    <p class="business-name">Harlow Lane Optical</p>
  </section>
</body>
</html>
```